Investment Company Business Card Design

We need a Business Card design for a new company based in Boston called "Velm Investment". We are cooperating with local real estate and construction companies. Our company is very actively and aggressively acquiring primarily residential investment properties either to buy and hold long term or for purposes or renovating and repositioning for re-sale in the market. In addition, we undertake some development projects and acquisitions as opportunities present themselves. the final design should contains information about “Velm" the river boat. we are tenacious, indomitable, and the business have a favorable wind throughout the voyage for all our investment.
sample Info. on Design:
Tusa Merrick
CEO
555-xxx-xxxx
418 Harlow St. Suite 507, Boston, MA 02111
Please provide a template also, that we can edit the info later.
Reason: i just got new LOGO Design attached will be use in Business Card Design.
Construction

```html
<!DOCTYPE html>
<html lang="en">
<head>
<meta charset="UTF-8">
<title>Velm Investment – Business Card</title>
<link rel="stylesheet" href="https://fonts.googleapis.com/css2?family=Open+Sans:ital,wght@0,400;0,700;1,400&display=swap">
<style>
  :root {
    --canvas-bg: #efefef;
    --card-bg: #1f2a2f;
    --sweep-tone: rgba(52, 66, 73, 0.55);
    --gold: #c9a24a;
    --text-light: #d6dadc;
    --text-muted: #b9bfc2;
  }
  * { margin: 0; padding: 0; box-sizing: border-box; }
  html, body {
    width: 1200px; height: 1000px; overflow: hidden;
    background: var(--canvas-bg);
    font-family: "Open Sans", Arial, sans-serif;
  }
  .stage { position: relative; width: 1200px; height: 1000px; }
  .card {
    position: absolute;
    width: 634px; height: 362px;
    background: var(--card-bg);
    overflow: hidden;
  }
  .card-front { left: 180px; top: 124px; }
  .card-back { left: 388px; top: 514px; }
  .card-sweep {
    position: absolute; inset: 0;
    background:
      radial-gradient(ellipse 70% 60% at 85% 95%, var(--sweep-tone), transparent 70%),
      radial-gradient(ellipse 50% 45% at 95% 10%, rgba(52, 66, 73, 0.35), transparent 70%);
  }
  .brand {
    position: absolute;
    display: flex; align-items: center;
    color: var(--gold);
    font-weight: 400;
    white-space: nowrap;
  }
  .brand-mark {
    border-radius: 50%;
    background: var(--gold);
    flex: none;
  }
  .card-front .brand { left: 52px; top: 150px; font-size: 40px; gap: 16px; }
  .card-front .brand-mark { width: 44px; height: 44px; }
  .card-back .brand { left: 38px; top: 68px; font-size: 22px; gap: 10px; }
  .card-back .brand-mark { width: 24px; height: 24px; }
  .person {
    position: absolute; right: 56px; top: 40px; text-align: right;
  }
  .person-name { color: var(--gold); font-weight: 700; font-size: 22px; line-height: 1.2; }
  .person-title { color: var(--text-muted); font-style: italic; font-size: 17px; line-height: 1.3; }
  .contact {
    position: absolute; left: 36px; top: 182px;
    list-style: none;
    color: var(--text-light);
    font-size: 17px; line-height: 24px;
  }
</style>
</head>
<body>
<main class="stage">

  <section class="card card-front" aria-label="Business card front">
    <div class="card-sweep" role="img" aria-label="Soft curved sweeps in dark slate tones across the card"></div>
    <div class="brand">Velm Investment<span class="brand-mark"></span></div>
  </section>

  <section class="card card-back" aria-label="Business card back">
    <div class="card-sweep" role="img" aria-label="Soft curved sweeps in dark slate tones across the card"></div>
    <div class="brand">Velm Investment<span class="brand-mark"></span></div>
    <div class="person">
      <div class="person-name">Tusa Merrick</div>
      <div class="person-title">CEO</div>
    </div>
    <ul class="contact">
      <li>555-xxx-xxxx</li>
      <li>555-xxx-xxxx</li>
      <li>418 Harlow St. Suite 507, Boston, MA 02111</li>
      <li>www.velminvest.com</li>
    </ul>
  </section>

</main>
</body>
</html>
```